Craft Beer Needs a Label/ Logo Design

Name: Lanternfall
(Lanternfall Ale, Lanternfall Pilsner, Lanternfall Stout)

We are looking for a logo-ed label that will resonate domestically and internationally for this new Craft Beer Brand.

Target Market(s)

Millenials

Logo Text

Lanternfall Pilsner

Logo styles of interest
Emblem Logo
Character Logo
Colors

Designer to choose colors to be used in the design.

Requirements
Must have
• A labled logo design -- "Lanternfall" is the name, but would like to see samples with "Ale", "Pilsner", or "Stout" after!

```html
<!DOCTYPE html>
<html lang="en">
<head>
<meta charset="utf-8">
<title>Lanternfall Beer Labels</title>
<link href="https://fonts.googleapis.com/css2?family=Smokum&display=swap" rel="stylesheet">
<style>
  :root {
    --paper: #ffffff;
    --label-black: #000000;
    --brass-gold: #a3861a;
  }
  html, body {
    margin: 0;
    padding: 0;
    overflow: hidden;
    background: var(--paper);
  }
  .sheet {
    position: relative;
    width: 941px;
    height: 1200px;
    overflow: hidden;
    background: var(--paper);
  }
  .beer-label {
    position: absolute;
    left: 142px;
    width: 656px;
    height: 494px;
  }
  .beer-label--pilser { top: 66px; }
  .beer-label--stout { top: 653px; }
  .label-body { fill: var(--label-black); }
  .label-frame {
    fill: none;
    stroke: var(--brass-gold);
    stroke-width: 9;
  }
  .brand-mark { fill: var(--brass-gold); }
  .brand-name,
  .beer-style {
    fill: var(--brass-gold);
    font-family: "Smokum", "Rye", serif;
    text-anchor: middle;
  }
  .brand-name { font-size: 86px; }
  .beer-style { font-size: 40px; letter-spacing: 1px; }
</style>
</head>
<body>
  <main class="sheet">
    <svg class="beer-label beer-label--pilser" viewBox="0 0 494 372" aria-labelledby="pilser-title">
      <title id="pilser-title">Lanternfall Pilser label</title>
      <path class="label-body" d="M33,35 Q248,-35 463,35 Q524,186 461,335 Q248,405 33,335 Q-33,186 33,35 Z"/>
      <path class="label-frame" d="M52,55 Q248,-5 442,55 Q503,186 440,318 Q248,392 52,318 Q-10,186 52,55 Z"/>
      <text class="brand-name" x="246" y="145" textLength="335" lengthAdjust="spacingAndGlyphs">LANTERNFALL</text>
      <circle class="brand-mark" cx="236" cy="197" r="42"/>
      <text class="beer-style" x="247" y="322" textLength="172" lengthAdjust="spacingAndGlyphs">-PILSER-</text>
    </svg>

    <svg class="beer-label beer-label--stout" viewBox="0 0 494 372" aria-labelledby="stout-title">
      <title id="stout-title">Lanternfall Stout label</title>
      <path class="label-body" d="M33,35 Q248,-35 463,35 Q524,186 461,335 Q248,405 33,335 Q-33,186 33,35 Z"/>
      <path class="label-frame" d="M52,55 Q248,-5 442,55 Q503,186 440,318 Q248,392 52,318 Q-10,186 52,55 Z"/>
      <text class="brand-name" x="246" y="145" textLength="335" lengthAdjust="spacingAndGlyphs">LANTERNFALL</text>
      <circle class="brand-mark" cx="236" cy="197" r="42"/>
      <text class="beer-style" x="247" y="318" textLength="160" lengthAdjust="spacingAndGlyphs">-STOUT-</text>
    </svg>
  </main>
</body>
</html>
```